Flyer-Design für Basilikum frisch-gruen-kochen-schlemmen
Zielgruppe
Hallo wir brauchen wieder Flyer für unser Lokal in Frankfurt. Es soll jetzt nichts besonderes beworben werden, also 'nur' Info wie das es uns gibt, wo wir zu finden sind, Kontaktdaten, Öffnungszeiten etc. Gedacht sind die Flyer quasi als Imageflyer.
Aufgabenstellung
Wir haben schonmal Flyer verwendet die ich selbst gestaltet habe, jetzt soll etwas neues, zeitgemässes her.
Göße: A6

```html
<!DOCTYPE html>
<html lang="de">
<head>
<meta charset="utf-8">
<title>Basilikum – Flyer</title>
<link href="https://fonts.googleapis.com/css2?family=Amatic+SC:wght@700&family=Kaushan+Script&family=Righteous&family=Yanone+Kaffeesatz:wght@400&display=swap" rel="stylesheet">
<style>
  :root {
    --paper: #ffffff;
    --mint: #dbe9dd;
    --mint-deep: #b9d6c6;
    --ink: #111111;
    --chili: #c9281e;
    --brand-red: #b23a2c;
    --brand-green: #6b8a55;
    --frame: #8a8a8a;
  }
  * { box-sizing: border-box; margin: 0; padding: 0; }
  html, body { width: 848px; height: 1200px; overflow: hidden; background: var(--paper); }
  body { position: relative; font-family: "Righteous", "Trebuchet MS", sans-serif; color: var(--ink); }

  .front-card {
    position: absolute; left: 121px; top: 46px; width: 598px; height: 424px;
    border: 1px solid var(--frame); background: var(--paper);
  }
  .front-art {
    position: absolute; left: 43px; top: 29px; width: 512px; height: 372px;
    background:
      radial-gradient(ellipse 38% 26% at 54% 66%, var(--chili) 0%, rgba(201,40,30,.8) 50%, rgba(201,40,30,0) 100%),
      linear-gradient(160deg, #cfe3d6 0%, var(--mint-deep) 55%, #c6ddd0 100%);
  }
  .love-badge {
    position: absolute; left: 66px; top: 48px; width: 138px; height: 138px;
    border-radius: 50%; background: var(--ink); color: var(--paper);
    font-family: "Kaushan Script", cursive; text-align: center;
  }
  .love-badge .small { display: block; font-size: 34px; line-height: 1; margin-top: 14px; }
  .love-badge .big { display: block; font-size: 56px; line-height: 1; margin-top: -4px; }

  .back-card {
    position: absolute; left: 120px; top: 491px; width: 598px; height: 424px;
    border: 1px solid var(--frame); background: var(--mint);
  }
  .title-block {
    position: absolute; left: 156px; top: -1px; width: 284px; height: 127px;
    background: var(--ink); color: var(--paper); text-align: center;
  }
  .title-block h1 {
    font-family: "Amatic SC", "Arial Narrow", sans-serif; font-weight: 700;
    font-size: 58px; line-height: 1; margin-top: 18px; letter-spacing: 1px;
  }
  .title-block p {
    font-family: "Yanone Kaffeesatz", "Arial Narrow", sans-serif; font-weight: 400;
    font-size: 27px; line-height: 1; margin-top: 6px;
  }
  .offer-list {
    position: absolute; left: 0; top: 138px; width: 100%; list-style: none;
    text-align: center; font-size: 17.5px; line-height: 27px; letter-spacing: 1px;
  }
  .opening-hours {
    position: absolute; left: 22px; top: 266px; font-size: 14.5px; line-height: 20px; letter-spacing: .6px;
  }
  .divider {
    position: absolute; left: 24px; top: 313px; width: 554px; height: 1.5px; background: var(--ink);
  }
  .contact {
    position: absolute; left: 23px; top: 330px; font-size: 15.5px; line-height: 20px; letter-spacing: .8px; font-style: normal;
  }
  .brand-mark {
    position: absolute; left: 414px; top: 333px; width: 160px; height: 60px;
    display: flex; align-items: center; gap: 8px;
  }
  .brand-mark .dot { width: 14px; height: 14px; background: var(--brand-green); flex: none; }
  .brand-mark .name { font-size: 27px; color: var(--brand-red); letter-spacing: .5px; }
  .brand-claim {
    position: absolute; left: 410px; top: 397px; width: 170px; text-align: center;
    font-size: 7.5px; color: var(--brand-red); letter-spacing: .4px;
  }

  .series-label {
    position: absolute; left: 42px; top: 955px; font-size: 13.5px; letter-spacing: .8px;
  }
  .series-motif { position: absolute; }
  .motif-cauliflower {
    left: 109px; top: 1010px; width: 171px; height: 155px; border-radius: 45%;
    background: radial-gradient(circle at 45% 60%, #f1ecd6 0%, #c9d9a4 45%, #8fb36a 75%, rgba(255,255,255,0) 100%);
  }
  .motif-radish {
    left: 352px; top: 978px; width: 150px; height: 188px; border-radius: 40%;
    background: linear-gradient(180deg, #9cc46d 0%, #6fa24d 40%, #d84a6d 70%, #b82048 100%);
  }
  .motif-broccoli {
    left: 571px; top: 995px; width: 144px; height: 160px; border-radius: 40%;
    background: radial-gradient(circle at 50% 35%, #3f7f2e 0%, #5c9a3e 45%, #a9cc85 80%, rgba(255,255,255,0) 100%);
  }
  .motif-tag {
    position: absolute; width: 46px; height: 46px; border-radius: 50%;
    background: var(--ink); color: var(--paper);
    font-family: "Kaushan Script", cursive; font-size: 12px; line-height: 12px;
    display: flex; align-items: center; justify-content: center; text-align: center;
  }
  .tag-cauliflower { left: 112px; top: 998px; }
  .tag-radish { left: 452px; top: 1021px; }
  .tag-broccoli { left: 602px; top: 1107px; }
</style>
</head>
<body>
  <section class="front-card">
    <div class="front-art" role="img" aria-label="Aquarell-Illustration roter Chilischoten auf mintgrünem Farbfleck"></div>
    <p class="love-badge"><span class="small">it's</span><span class="big">Love</span></p>
  </section>

  <section class="back-card">
    <header class="title-block">
      <h1>BASILIKUM</h1>
      <p>vegane Küche in Frankfurt</p>
    </header>

    <ul class="offer-list">
      <li>- täglich wechselnde Speisekarte</li>
      <li>- sonntags veganer Brunch</li>
      <li>- BIO -Cocktails, -Limonaden, -Weine</li>
    </ul>

    <p class="opening-hours">
      Mo. Ruhetag,<br>
      Di. - Sa.&nbsp;&nbsp; 18 - 23 Uhr | So. Brunch&nbsp; 10 - 15 Uhr | ab 18 Uhr Abendkarte
    </p>

    <div class="divider"></div>

    <address class="contact">
      Am Lindenhof 14<br>
      60389 Frankfurt<br>
      069 - 555 01 234<br>
      hallo@basilikum-frankfurt.de
    </address>

    <div class="brand-mark">
      <span class="dot"></span>
      <span class="name">BASILIKUM</span>
    </div>
    <p class="brand-claim">FRISCH · GRUEN · KOCHEN · SCHLEMMEN</p>
  </section>

  <p class="series-label">weitere mögl. Motive einer Serie:</p>
  <div class="series-motif motif-cauliflower" role="img" aria-label="Aquarell-Illustration eines Blumenkohls"></div>
  <div class="series-motif motif-radish" role="img" aria-label="Aquarell-Illustration eines Radieschenbunds"></div>
  <div class="series-motif motif-broccoli" role="img" aria-label="Aquarell-Illustration von Brokkoli"></div>
  <p class="motif-tag tag-cauliflower">Cauli<br>flower</p>
  <p class="motif-tag tag-radish">Radish</p>
  <p class="motif-tag tag-broccoli">Broccoli</p>
</body>
</html>
```